Varden Homes needs a stationery design

I need a stationary design for my new custom home building company. Our company deals with very high end and luxurious homes so i need a stationary design that shows strength, elegance, and trust.
The final version should be trendy, clean... only 2 colours (green + grey/black) and professional.
#1: Business Cards (design on 2 sides)
#2: Letterhead (word format)
#3: Cover Page and back cover for proposals
#4: Envelopes,
#5: Thank You card,
#6: Presentation Folder
Logo is attached. Logo can be reversed out (will attach once available). Logo can be stacked or horizontal (provided as horizontal).
The business cards need to be two sided with the company logo and website on the front (www.vardenhomes-example.com and contact info on the back.
The contact info can be made up temporarily and once the final design is chosen, i will provide you with all the correct contact information during the revision stage.
id like to see examples with black, white, blue, red, purple. (You should not try to use all these in one design)
I have attached my company's logo in 3 different colours and a few sample business cards that i found on the internet. I would like to see unique designs though, don't try to imitate the examples
Updates
Dear designers,
I have also attached the .eps and ai files for the 3 different coloured logos.
Please notify me if you need anything else to complete your work
Best Regards,
Varden

```html
<!DOCTYPE html>
<html lang="en">
<head>
<meta charset="UTF-8">
<title>Varden Homes – Business Card</title>
<link href="https://fonts.googleapis.com/css2?family=Arimo:wght@400;700&family=Questrial&display=swap" rel="stylesheet">
<style>
  :root {
    --bg: #e9e9ea;
    --card-dark-1: #2a2a2b;
    --card-dark-2: #3c3c3d;
    --card-white: #ffffff;
    --ink: #3a3a3a;
    --ink-soft: #5a5a5a;
    --navy: #1f2a6b;
    --grey-dark: #4a4a4b;
    --grey-mid: #9a9a9b;
    --grey-light: #d4d4d5;
    --line: #bdbdbd;
  }
  * { box-sizing: border-box; margin: 0; padding: 0; }
  html, body { width: 1200px; height: 1000px; overflow: hidden; }
  body {
    background: var(--bg);
    font-family: "Arimo", Arial, sans-serif;
    position: relative;
  }
  .card {
    position: absolute;
    left: 320px;
    width: 560px;
    height: 320px;
    overflow: hidden;
    box-shadow: 0 10px 28px rgba(0,0,0,.18);
  }

  /* Front */
  .card-front {
    top: 110px;
    background: linear-gradient(160deg, var(--card-dark-2) 0%, var(--card-dark-1) 70%);
  }
  .front-brand {
    position: absolute;
    left: 0; right: 0; top: 118px;
    display: flex; align-items: center; justify-content: center; gap: 14px;
  }
  .brand-square { width: 16px; height: 16px; background: #fff; }
  .front-brand .brand-name {
    font-family: "Questrial", sans-serif;
    color: #fff;
    font-size: 40px;
    letter-spacing: 3px;
  }
  .front-footer {
    position: absolute; left: 0; right: 0; bottom: 0; height: 56px;
    border-top: 2px solid #6a6a6b;
    background: var(--card-dark-1);
    display: flex; align-items: center; justify-content: center;
  }
  .front-footer .web { color: #fff; font-size: 15px; letter-spacing: .3px; }

  /* Back */
  .card-back {
    top: 560px;
    background: var(--card-white);
  }
  .back-bands { position: absolute; inset: 0; }
  .identity {
    position: absolute; left: 40px; top: 46px; width: 230px;
  }
  .identity .brand-name {
    font-family: "Questrial", sans-serif;
    color: var(--navy);
    font-size: 28px;
    letter-spacing: 1px;
  }
  .person-name {
    margin-top: 26px;
    font-family: "Questrial", sans-serif;
    font-size: 25px;
    color: var(--ink);
    letter-spacing: 1px;
    padding-bottom: 4px;
    border-bottom: 1px solid var(--ink);
  }
  .person-role { margin-top: 6px; font-size: 14px; color: var(--ink-soft); }
  .divider-bars { position: absolute; left: 300px; top: 96px; width: 8px; }
  .divider-bars span { display: block; width: 8px; }
  .bar-dark { height: 60px; background: var(--grey-dark); }
  .bar-light { height: 38px; margin-top: 10px; background: var(--grey-light); }
  .contact { position: absolute; left: 326px; top: 90px; list-style: none; }
  .contact li {
    display: flex; gap: 10px; align-items: flex-start;
    font-size: 13px; line-height: 16px; color: var(--ink);
    margin-bottom: 8px;
  }
  .contact svg { flex: none; width: 14px; height: 14px; margin-top: 1px; fill: var(--grey-dark); }
  .contact .label { display: inline-block; width: 48px; }
</style>
</head>
<body>

<section class="card card-front" aria-label="Business card front">
  <div class="front-brand">
    <span class="brand-square"></span>
    <span class="brand-name">Varden Homes</span>
  </div>
  <footer class="front-footer">
    <span class="web">www.vardenhomes-example.com</span>
  </footer>
</section>

<section class="card card-back" aria-label="Business card back">
  <svg class="back-bands" viewBox="0 0 560 320" preserveAspectRatio="none" aria-hidden="true">
    <polygon points="0,260 300,260 312,276 312,320 0,320" fill="#4a4a4b"/>
    <polygon points="0,270 298,270 306,280 0,280" fill="#6d6d6e"/>
    <polygon points="330,250 560,250 560,320 346,320" fill="#a3a3a4"/>
    <polygon points="346,292 560,292 560,320 352,320" fill="#c4c4c5"/>
  </svg>

  <div class="identity">
    <div class="brand-name">Varden Homes</div>
    <div class="person-name">MARCUS HALE</div>
    <div class="person-role">Managing director</div>
  </div>

  <div class="divider-bars"><span class="bar-dark"></span><span class="bar-light"></span></div>

  <ul class="contact">
    <li>
      <svg viewBox="0 0 14 14"><path d="M7 1 1 6.5h2V13h3V9h2v4h3V6.5h2z"/></svg>
      <span>Varden Homes Street<br>Varden Homes Street, 01234</span>
    </li>
    <li>
      <svg viewBox="0 0 14 14"><path d="M7 1a6 6 0 1 0 3 11.2l-.6-1A4.8 4.8 0 1 1 11.8 7v.8c0 .6-.4 1-.9 1s-.9-.4-.9-1V4.5H8.9v.5A3 3 0 1 0 9.3 9a2 2 0 0 0 3.7-1.2V7A6 6 0 0 0 7 1zm0 7.8A1.8 1.8 0 1 1 7 5.2a1.8 1.8 0 0 1 0 3.6z"/></svg>
      <span>hello@vardenhomes-example.com<br>www.vardenhomes-example.com</span>
    </li>
    <li>
      <svg viewBox="0 0 14 14"><path d="M3.2 1.5 5 1l1.3 3-1.2 1a7 7 0 0 0 3.9 3.9l1-1.2 3 1.3-.5 1.8c-.2.6-.8 1-1.4.9A10.5 10.5 0 0 1 2.3 2.9c-.1-.6.3-1.2.9-1.4z"/></svg>
      <span><span class="label">Tel.</span>+012 555 0148<br><span class="label">Fax</span>+012 555 0148<br><span class="label">Mobile</span>+012 555 0148</span>
    </li>
  </ul>
</section>

</body>
</html>
```